20 year old business card needs re-design

We need to redesign our corporate business card look. We need something that appears more modern, eye catchy but professional.

Target Market(s)

manufacturing industry

Industry/Entity Type

Manufacturer

Contact Information for Business Card

One side can have the logo. Other side can have contact information.

Font styles to use
Serif

Colors
3277b5
33b8a4
ffffff

Requirements
Must have
• Eye catchy - need to standout from the crowd. company logo cannot change. Full name, job title, phone number and email address.
Should not have
• Fax, business address is not necessary.

```html
<!DOCTYPE html>
<html lang="en">
<head>
<meta charset="utf-8">
<title>Corvane Global – Business Card</title>
<link rel="stylesheet" href="https://fonts.googleapis.com/css2?family=Karla:wght@400;700&display=swap">
<style>
  :root {
    --teal: #1bb3a0;
    --teal-deep: #17a996;
    --teal-light: #2fc0ac;
    --mint: #b3e0d8;
    --ink: #2b2b2b;
    --text: #333333;
    --white: #ffffff;
    --backdrop: #eef1f0;
  }
  * { margin: 0; padding: 0; box-sizing: border-box; }
  html, body {
    width: 1200px; height: 1200px; overflow: hidden;
    background: var(--backdrop);
    font-family: "Karla", Arial, sans-serif;
  }
  .canvas { position: relative; width: 1200px; height: 1200px; }

  .card {
    position: absolute; left: 250px; width: 700px; height: 400px;
    box-shadow: 0 6px 18px rgba(0,0,0,0.18);
    overflow: hidden;
  }

  /* Front */
  .card-front { top: 150px; background: var(--teal); }
  .card-front .blueprint-area {
    position: absolute; inset: 0;
    background: linear-gradient(135deg, var(--teal-light) 0%, var(--teal) 55%, var(--teal-deep) 100%);
  }
  .card-front .edge-tab {
    position: absolute; left: 0; top: 300px; width: 44px; height: 96px;
    background: var(--white);
  }
  .card-front .brand {
    position: absolute; right: 60px; top: 236px; text-align: left;
  }
  .card-front .wordmark {
    font-weight: 700; font-size: 52px; color: var(--white);
    letter-spacing: -1px; line-height: 1;
  }
  .card-front .website {
    margin-top: 10px; font-size: 19px; color: var(--white);
    letter-spacing: 0.3px; padding-left: 44px;
  }

  /* Back */
  .card-back { top: 650px; background: var(--mint); color: var(--text); }
  .card-back .wordmark {
    position: absolute; left: 38px; top: 50px;
    font-weight: 700; font-size: 50px; color: var(--ink);
    letter-spacing: -1px; line-height: 1;
  }
  .card-back .tagline {
    position: absolute; left: 38px; top: 170px;
    font-size: 16px; line-height: 21px;
  }
  .card-back .contact {
    position: absolute; left: 40px; top: 250px;
    font-size: 18px; line-height: 23px; letter-spacing: 0.2px;
  }
  .card-back .certification {
    position: absolute; left: 38px; top: 340px; font-size: 16px;
  }
  .card-back .name-plate {
    position: absolute; right: 0; top: 252px; width: 296px; height: 100px;
    display: flex;
  }
  .card-back .name-box {
    flex: 1; background: var(--white);
    display: flex; flex-direction: column; align-items: center; justify-content: center;
  }
  .card-back .person-name {
    font-size: 29px; font-weight: 400; color: var(--ink); letter-spacing: 0.5px; line-height: 1.1;
  }
  .card-back .person-title {
    font-size: 16px; color: var(--teal); margin-top: 4px;
  }
  .card-back .name-tab { width: 39px; background: var(--teal); }
</style>
</head>
<body>
<main class="canvas">
  <section class="card card-front">
    <div class="blueprint-area" role="img" aria-label="Faint white engineering blueprint of gears and machine parts over teal"></div>
    <div class="edge-tab"></div>
    <div class="brand">
      <div class="wordmark">Corvane Global</div>
      <div class="website">CorvaneGlobal.com</div>
    </div>
  </section>

  <section class="card card-back">
    <div class="wordmark">Corvane Global</div>
    <p class="tagline">International manufacturing solutions<br>for OEM customers in North America</p>
    <p class="contact">Main: 555-014-2290 xt 201<br>lena@corvaneglobal.com</p>
    <p class="certification">TS16949 &amp; ISO9001 Certified Facilities</p>
    <div class="name-plate">
      <div class="name-box">
        <span class="person-name">Lena Marsh</span>
        <span class="person-title">Senior Project Manager</span>
      </div>
      <div class="name-tab"></div>
    </div>
  </section>
</main>
</body>
</html>
```